Trifold B2B flyer for software consulting/software futureproofness check / IT company

We need a flyer for a consulting offer for the company "VORANTIK GmbH".

The service involves the analysis and evaluation of software systems in companies; the target group consists of managing directors and IT managers of medium-sized companies in various industries.

The flyer should be modern, uncluttered, serious, and professional. It must inspire trust. A dark background would be preferable.

For content and layout, see PDF/PPTX "Software-Zukunft-Schnellcheck-Konzept.pptx|.pdf".

In the appendix you will find further examples of VORANTIK designs, as well as the logo and other images.

-----------
We need a flyer for a consulting offering for the company “VORANTIK GmbH”.

The offering focuses on the analysis and evaluation of software systems within companies. The target audience is managing directors/CEOs and IT managers of mid-sized companies across various industries.

The flyer should be modern, clean, serious, and professional. It must build trust. A dark background is preferred.

Please refer to the PDF/PPTX “Software-Horizont-Schnellcheck-konzept.pptx|.pdf” for the content and the layout/ordering of the sections.

Attached you will also find additional examples of VORANTIK designs, as well as the logo and further images.

Target Market(s)

Medium businesses, various industries. Target group: CEO, CIO, IT lead

Industry/Entity Type

Medium-Businesses, various Industries.

Font styles to use
Sans Serif
Other font styles liked:
• Myriad

Colors

Designer to choose colors to be used in the design.

Requirements
Must have
• Branding of my company, professional, stylish, clean, trustful design

```html
<!DOCTYPE html>
<html lang="de">
<head>
<meta charset="utf-8">
<title>Software-Horizont-Schnellcheck</title>
<link href="https://fonts.googleapis.com/css2?family=Arimo:wght@400;700&display=swap" rel="stylesheet">
<style>
  :root {
    --bg-top: #0c2443;
    --bg-bottom: #01102c;
    --accent: #3571b9;
    --accent-text: #3a78c2;
    --text: #e9eef6;
    --box-text: #0e2b56;
    --fold: #d8dee8;
  }
  html, body { margin: 0; padding: 0; overflow: hidden; }
  body { width: 1200px; height: 848px; }
  .flyer {
    position: relative; width: 1200px; height: 848px; overflow: hidden;
    background: linear-gradient(180deg, var(--bg-top) 0%, var(--bg-bottom) 100%);
    font-family: "Arimo", "Helvetica Neue", Arial, sans-serif;
    color: var(--text);
  }
  .abs { position: absolute; }
  .fold-mark { position: absolute; width: 1.5px; height: 20px; background: var(--fold); }
  .title { left: 43px; top: 40px; font-size: 20px; font-weight: 700; color: var(--accent-text); margin: 0; white-space: nowrap; }
  .subtitle { left: 485px; top: 40px; font-size: 19px; font-weight: 400; margin: 0; white-space: nowrap; }
  .intro-box {
    left: 81px; top: 91px; width: 1099px; height: 61px; border-radius: 7px;
    background: var(--accent); color: var(--box-text); box-sizing: border-box;
    padding: 10px 0 0 20px; font-size: 16px; line-height: 20.5px;
  }
  .intro-box p { margin: 0; white-space: nowrap; }
  .col-head { font-size: 20px; font-weight: 700; color: var(--accent-text); margin: 0; top: 199px; white-space: nowrap; }
  .divider { width: 4px; border-radius: 2px; background: var(--accent); top: 209px; height: 386px; }
  .list { list-style: none; margin: 0; padding: 0; font-size: 15.5px; line-height: 19px; }
  .list li { position: absolute; left: 0; white-space: nowrap; }
  .list li::before {
    content: ""; position: absolute; left: -16px; top: 7px;
    width: 6px; height: 6px; border-radius: 50%; background: var(--text);
  }
  .list b { font-weight: 700; }
  .questions { left: 81px; top: 255px; width: 275px; }
  .steps { left: 519px; top: 255px; width: 240px; }
  .results { left: 889px; top: 255px; width: 285px; }
  .small-head { font-size: 18px; font-weight: 700; color: var(--accent-text); margin: 0; }
  .small-list { list-style: none; margin: 0; padding: 0; font-size: 12.5px; line-height: 15.5px; }
  .small-list li { position: absolute; left: 0; white-space: nowrap; }
  .small-list li::before, .price-list li::before {
    content: ""; position: absolute; left: -18px; top: 6px; width: 3px; height: 3px; background: var(--text);
  }
  .price-list { list-style: none; margin: 0; padding: 0; font-size: 16px; line-height: 20px; }
  .price-list li { position: absolute; left: 0; white-space: nowrap; }
  .price-list li::before { left: -17px; top: 8px; width: 4px; height: 4px; }
  .upgrade { left: 869px; top: 778px; font-size: 14px; line-height: 24px; margin: 0; white-space: nowrap; }
  .upgrade b { color: var(--accent-text); }
</style>
</head>
<body>
<main class="flyer">
  <span class="fold-mark" style="left:404px;top:0"></span>
  <span class="fold-mark" style="left:808px;top:0"></span>
  <span class="fold-mark" style="left:405px;top:828px"></span>
  <span class="fold-mark" style="left:809px;top:828px"></span>

  <h1 class="abs title">Software-Horizont-Schnellcheck</h1>
  <p class="abs subtitle">Bestandssysteme: weiter investieren,&nbsp; modernisieren oder ersetzen?</p>

  <svg class="abs" style="left:20px;top:91px" width="47" height="61" viewBox="0 0 47 61">
    <path d="M2 2 L45 28 Q47 30.5 45 33 L2 59 Q0 60 0 57 V4 Q0 1 2 2 Z" fill="var(--accent)"/>
  </svg>
  <div class="abs intro-box">
    <p>Der <i>Schnellcheck</i> dient der schnellen Orientierung und Objektivierung.</p>
    <p>Er stellt die Basis für eine detaillierte Analyse des Bestandssystems in Punkto Zukunftsfähigkeit und Handlungsoptionen.</p>
  </div>

  <h2 class="abs col-head" style="left:41px">Fragestellungen</h2>
  <h2 class="abs col-head" style="left:479px">Vorgehen</h2>
  <h2 class="abs col-head" style="left:849px">Ergebnisse / Lieferobjekte</h2>

  <span class="abs divider" style="left:368px"></span>
  <span class="abs divider" style="left:760px"></span>
  <svg class="abs" style="left:368px;top:346px" width="82" height="104" viewBox="0 0 82 104">
    <path d="M0 0 L78 47 Q82 52 78 57 L0 104 Z" fill="var(--accent)"/>
  </svg>
  <svg class="abs" style="left:760px;top:346px" width="82" height="104" viewBox="0 0 82 104">
    <path d="M0 0 L78 47 Q82 52 78 57 L0 104 Z" fill="var(--accent)"/>
  </svg>

  <ul class="abs list questions">
    <li style="top:0">Was sind die <b>realen Risiken</b> (Betrieb,<br>Stabilität, Abhängigkeiten, Know-<br>how)?</li>
    <li style="top:89px">Wo liegen die <b>größten Kostentreiber</b><br>(Run-Kosten, Change-Kosten,<br>Folgekosten)?</li>
    <li style="top:178px">Welche drei Wege sind grundsätzlich<br>realistisch: <b>Invest / Modernize /<br>Replace</b>?</li>
    <li style="top:267px">Was müssen wir <b>jetzt</b> wissen, um<br>innerhalb von 5–10 Tagen sauber<br>entscheiden zu können?</li>
  </ul>

  <svg class="abs" style="left:452px;top:250px" width="26" height="310" viewBox="0 0 26 310">
    <line x1="13" y1="21" x2="13" y2="289" stroke="var(--accent)" stroke-width="3.5"/>
    <g fill="var(--bg-top)" stroke="var(--accent)" stroke-width="3.5">
      <circle cx="13" cy="13" r="9.5"/>
      <circle cx="13" cy="100" r="9.5"/>
      <circle cx="13" cy="210" r="9.5" fill="#071a38"/>
      <circle cx="13" cy="297" r="9.5" fill="#051735"/>
    </g>
  </svg>

  <ul class="abs list steps">
    <li style="top:0"><b>Kickoff (60–90 Min):</b> Ziel,<br>Kontext, Entscheidungsdruck,<br>verfügbare Artefakte</li>
    <li style="top:89px"><b>Sichtung &amp; Analyse:</b> max. 10<br>Artefakte (Kosten, Incidents,<br>Roadmap, Architektur-Skizze,<br>Vendor-Info)</li>
    <li style="top:197px"><b>2 Interviews (je 60–90 Min):</b><br>CIO/Owner + Head of<br>Engineering/Tech Lead</li>
    <li style="top:286px"><b>Ergebnisgespräch (60 Min):</b><br>Ergebnisse, Lücken, Empfehlung,<br>nächster Schritt</li>
  </ul>

  <ul class="abs list results">
    <li style="top:0"><b>Decision Snapshot:</b> Status, Top-<br>Risiken, wesentliche TCO-Treiber, offene<br>Entscheidungsfragen (One-Pager)</li>
    <li style="top:89px"><b>3-Optionen-Skizze:</b> Modernize /<br>Replace / Invest mit Pros/Cons und<br>Abhängigkeiten (One-Pager)</li>
    <li style="top:178px"><b>Gap-Liste:</b> Welche Informationen fehlen<br>für eine saubere Entscheidung (Max. 10<br>Punkte)</li>
    <li style="top:267px"><b>Go/No-Go-Empfehlung:</b><br>Mögliche nächste Schritte und<br>Handlungsoptionen</li>
  </ul>

  <h3 class="abs small-head" style="left:444px;top:639px">Scope:</h3>
  <ul class="abs small-list" style="left:485px;top:667px">
    <li style="top:0">1 System</li>
    <li style="top:23px">1–2 Calls + Doku-Sichtung</li>
    <li style="top:47px">Ergebnis als kompakte Entscheidungsunterlagen</li>
  </ul>

  <h3 class="abs small-head" style="left:444px;top:762px">Nicht enthalten:</h3>
  <ul class="abs small-list" style="left:485px;top:790px">
    <li style="top:0">Detail-Spezifikation, Ausschreibung, Umsetzung,<br>Tool-Auswahlprozess im Vollumfang</li>
  </ul>

  <h3 class="abs small-head" style="left:849px;top:640px;font-size:19.5px">Preis &amp; Dauer:</h3>
  <ul class="abs price-list" style="left:889px;top:669px">
    <li style="top:0"><b>Preis: 3.500–5.000 €</b> (zzgl. USt)</li>
    <li style="top:27px"><b>Dauer: 1 Woche</b></li>
  </ul>

  <p class="abs upgrade">Upgrade möglich zum umfassenden <b>Software-</b><br><b>Horizont-Check</b></p>
</main>
</body>
</html>
```